New Business Card : Logo provided (black&red)

Use logo to ascertain colours.
Front of card :
Logo
Director : Darren Kellworth
ABN : 47302961
T : 0458 712 064
E : trimvolt@pelmarix.com
W : trimvoltfitness.net.au

Back of card :
Outdoor Group Training
Harrowvale Rowing Club
42 Pellinore Road
Kestrelton WA 6031

Personal Training
Greywater Bay Fitness Studio
518 Marrowdene Street
Kestrelton WA 6031

Logo's attached are low resolution apparently so will look into why that is and update as soon as I can.  

Logo's updated.

```html
<!DOCTYPE html>
<html lang="en">
<head>
<meta charset="utf-8">
<title>Trimvolt Fitness – Business Card</title>
<link rel="stylesheet" href="https://fonts.googleapis.com/css2?family=Jost:wght@400;500;600&display=swap">
<style>
  :root {
    --stage: #e4e4e4;
    --brand-red: #e8292b;
    --brand-red-light: #f05a3e;
    --ink: #231f20;
    --ink-soft: #5a5a5a;
    --paper: #fdfdfd;
    --paper-shade: #f1f1f1;
    --white: #ffffff;
  }
  * { box-sizing: border-box; margin: 0; padding: 0; }
  html, body {
    width: 1200px; height: 900px; overflow: hidden;
    background: radial-gradient(circle at 50% 45%, #f4f4f4 0%, var(--stage) 75%);
    font-family: "Jost", "Futura", sans-serif;
  }
  .canvas {
    width: 1200px; height: 900px;
    display: flex; align-items: center; justify-content: center; gap: 40px;
  }
  .card {
    position: relative;
    width: 540px; height: 330px;
    border-radius: 2px;
    box-shadow: 0 10px 24px rgba(0,0,0,0.18);
    overflow: hidden;
  }

  /* Back of card */
  .card--back {
    background: radial-gradient(circle at 58% 40%, var(--brand-red-light) 0%, var(--brand-red) 60%, #dc2226 100%);
    color: var(--white);
  }
  .card--back .wordmark { position: absolute; left: 110px; top: 128px; color: var(--white); }
  .card--back .wordmark__dot { background: var(--white); }
  .location {
    position: absolute; font-size: 13px; line-height: 1.3; font-weight: 400;
    font-style: normal; white-space: nowrap;
  }
  .location__title { font-weight: 600; font-size: 13.5px; }
  .location--outdoor { left: 40px; bottom: 34px; }
  .location--studio { right: 40px; top: 40px; text-align: right; }

  /* Front of card */
  .card--front {
    background: linear-gradient(135deg, var(--paper) 0%, var(--paper-shade) 100%);
    color: var(--ink-soft);
  }
  .card--front .wordmark { position: absolute; left: 262px; top: 72px; color: var(--ink); }
  .card--front .wordmark__dot { background: var(--brand-red); }
  .person { position: absolute; left: 300px; top: 140px; white-space: nowrap; }
  .person__name { color: var(--brand-red); font-weight: 600; font-size: 15px; }
  .person__role { font-size: 15px; margin-top: 2px; }
  .contact-list { list-style: none; margin-top: 12px; }
  .contact-list__item { display: flex; align-items: center; gap: 12px; font-size: 15px; line-height: 1.35; }
  .contact-list__icon { width: 13px; height: 13px; flex: none; fill: var(--brand-red); }
  .abn { position: absolute; left: 40px; bottom: 30px; font-size: 14px; color: var(--ink); letter-spacing: 0.5px; }

  /* Brand name stand-in */
  .wordmark {
    display: flex; align-items: center; gap: 10px;
    font-weight: 600; font-size: 22px; letter-spacing: 0.5px;
    text-transform: uppercase; white-space: nowrap; line-height: 1;
  }
  .wordmark__dot { width: 28px; height: 28px; border-radius: 50%; flex: none; }
</style>
</head>
<body>
<main class="canvas">

  <section class="card card--back" aria-label="Back of business card">
    <div class="wordmark"><span class="wordmark__dot"></span><span>Trimvolt Fitness</span></div>

    <address class="location location--studio">
      <p class="location__title">Personal Training</p>
      <p>Greywater Bay Fitness Studio</p>
      <p>518 Marrowdene Street</p>
      <p>Kestrelton WA 6031</p>
    </address>

    <address class="location location--outdoor">
      <p class="location__title">Outdoor Group Training</p>
      <p>Harrowvale Rowing Club</p>
      <p>42 Pellinore Road</p>
      <p>Kestrelton WA 6031</p>
    </address>
  </section>

  <section class="card card--front" aria-label="Front of business card">
    <div class="wordmark"><span class="wordmark__dot"></span><span>Trimvolt Fitness</span></div>

    <div class="person">
      <p class="person__name">Darren Kellworth</p>
      <p class="person__role">Director</p>
      <ul class="contact-list">
        <li class="contact-list__item">
          <svg class="contact-list__icon" viewBox="0 0 16 16" aria-hidden="true"><path d="M3 2h3l1.5 3.5-2 1.3a8 8 0 0 0 3.7 3.7l1.3-2L14 10v3a1 1 0 0 1-1 1A11 11 0 0 1 2 3a1 1 0 0 1 1-1z"/></svg>
          <span>0458 712 064</span>
        </li>
        <li class="contact-list__item">
          <svg class="contact-list__icon" viewBox="0 0 16 16" aria-hidden="true"><path d="M1 3h14v10H1zM2.2 4.2v.4L8 8.6l5.8-4v-.4zM2.2 6v5.8h11.6V6L8 10z"/></svg>
          <span>trimvolt@pelmarix.com</span>
        </li>
        <li class="contact-list__item">
          <svg class="contact-list__icon" viewBox="0 0 16 16" aria-hidden="true"><path d="M8 1a7 7 0 1 0 0 14A7 7 0 0 0 8 1zm0 1.3c.8 0 1.7 1.4 2 3.7H6c.3-2.3 1.2-3.7 2-3.7zM5.8 7.2h4.4a12 12 0 0 1 0 1.6H5.8a12 12 0 0 1 0-1.6zM2.4 7.2h2.2v1.6H2.4a5.7 5.7 0 0 1 0-1.6zm9 0h2.2a5.7 5.7 0 0 1 0 1.6h-2.2a13 13 0 0 0 0-1.6zM6 10h4c-.3 2.3-1.2 3.7-2 3.7S6.3 12.3 6 10z"/></svg>
          <span>trimvoltfitness.net.au</span>
        </li>
      </ul>
    </div>

    <p class="abn">ABN : 47302961</p>
  </section>

</main>
</body>
</html>
```